Business Card - Cooperate

Business Card for Larkfield Management Consulting

Target Market(s)

Corparte - b2B

Industry/Entity Type

Management Consulting - Professional Services

Contact Information for Business Card

Company Name , Slogan , Dummy Address,

Requirements
Must have
• Reach your Full Potential

```html
<!DOCTYPE html>
<html lang="en">
<head>
<meta charset="utf-8">
<title>Larkfield Management Consulting — Business Card</title>
<link href="https://fonts.googleapis.com/css2?family=Montserrat:wght@700;800&family=Nunito+Sans:wght@400;600&display=swap" rel="stylesheet">
<style>
  :root {
    --navy: #2b2f7e;
    --royal: #2e4fa8;
    --sky: #0b8fd3;
    --lime: #7dc242;
    --ink: #1c1c24;
    --paper: #ffffff;
    --silver: #d3d6db;
    --stage: #e9eaee;
  }
  * { box-sizing: border-box; margin: 0; padding: 0; }
  html, body { width: 1200px; height: 900px; overflow: hidden; }
  body {
    background: var(--stage);
    font-family: "Nunito Sans", sans-serif;
    display: flex; flex-direction: column; align-items: center; justify-content: center; gap: 40px;
  }
  .card {
    position: relative; width: 700px; height: 400px; overflow: hidden;
    box-shadow: 0 6px 18px rgba(0,0,0,.18);
  }

  /* front */
  .card-front { background: var(--paper); }
  .edge-bands { position: absolute; left: 0; bottom: 0; width: 700px; height: 120px; }
  .brand-name {
    display: flex; align-items: center; gap: 12px;
    font-family: "Montserrat", sans-serif; font-weight: 700; font-size: 42px; color: var(--navy);
  }
  .card-front .brand-name { position: absolute; left: 48px; top: 126px; }
  .brand-dot { width: 30px; height: 30px; border-radius: 50%; background: var(--royal); }
  .divider { position: absolute; left: 330px; top: 70px; width: 2px; height: 240px; background: var(--lime); }
  .details { position: absolute; left: 356px; top: 66px; color: var(--ink); }
  .person {
    font-family: "Montserrat", sans-serif; font-weight: 800; font-size: 25px; line-height: 1;
    text-transform: uppercase;
  }
  .person .first { color: var(--royal); }
  .person .last { color: var(--lime); }
  .role, .address { font-size: 16px; line-height: 1.3; }
  .role { margin-top: 6px; }
  .address { margin-top: 8px; }
  .contacts { list-style: none; margin-top: 8px; font-size: 16px; line-height: 1.35; }
  .contacts li { display: flex; align-items: center; gap: 8px; }
  .contacts svg { width: 14px; height: 14px; flex: none; }

  /* back */
  .card-back {
    background: linear-gradient(172deg, var(--navy) 0%, var(--royal) 30%, var(--sky) 62%, var(--lime) 100%);
    display: flex; flex-direction: column; align-items: center; justify-content: center;
  }
  .card-back .brand-name { font-size: 76px; color: var(--silver); gap: 20px; }
  .card-back .brand-dot { width: 50px; height: 50px; background: var(--silver); }
  .slogan {
    margin-top: 34px;
    font-family: "Nunito Sans", sans-serif; font-weight: 400; font-size: 20px;
    color: var(--paper);
  }
</style>
</head>
<body>

<section class="card card-front" aria-label="Business card front">
  <svg class="edge-bands" viewBox="0 0 700 120" aria-hidden="true">
    <polygon points="0,0 210,92 700,92 700,120 0,120" fill="#7dc242"/>
    <polygon points="200,96 700,96 700,120 270,120" fill="#2b2f7e"/>
  </svg>

  <div class="brand-name"><span class="brand-dot"></span>Larkfield</div>

  <div class="divider"></div>

  <div class="details">
    <h1 class="person"><span class="first">Dana</span> <span class="last">Whitcombe</span></h1>
    <p class="role">Co-Founder<br>Management Consulting<br>Professional Services</p>
    <p class="address">1420 Harbour Lane, Suite 310,<br>Oakridge, ON K7P 3M2</p>
    <ul class="contacts">
      <li><svg viewBox="0 0 16 16"><path d="M4 1.5 6.5 4 5 6c1 2 3 4 5 5l2-1.5 2.5 2.5-1.8 2.2C8 14 2 8 1.8 3.3Z" fill="#7dc242"/></svg>555-014-2287</li>
      <li><svg viewBox="0 0 16 16"><rect x="1" y="3" width="14" height="10" fill="#7dc242"/><path d="M1 3 8 9l7-6" fill="none" stroke="#fff" stroke-width="1.4"/></svg>hello@larkfieldmail.com</li>
      <li><svg viewBox="0 0 16 16"><circle cx="8" cy="8" r="7" fill="#7dc242"/><path d="M1 8h14M8 1c-3 4-3 10 0 14M8 1c3 4 3 10 0 14" fill="none" stroke="#fff" stroke-width="1"/></svg>www.larkfieldconsult.com</li>
    </ul>
  </div>
</section>

<section class="card card-back" aria-label="Business card back">
  <div class="brand-name"><span class="brand-dot"></span>Larkfield</div>
  <p class="slogan">Reach your full potential</p>
</section>

</body>
</html>
```